WPF Application Design

I require a design for a WPF application. I have the screenshots which needs to be redesigned for WPF application. Screens have different standard controls used, designer should suggest best placement and styling for the screens.

```html
<!DOCTYPE html>
<html lang="en">
<head>
<meta charset="utf-8">
<title>Course Template</title>
<link rel="stylesheet" href="https://fonts.googleapis.com/css2?family=Source+Sans+3:wght@300;400&display=swap">
<style>
  :root {
    --brand: #1f75be;
    --page: #ffffff;
    --divider: #e8e8e8;
    --text: #3a3a3a;
    --muted: #c4c4c4;
    --field-border: #9a9a9a;
    --control-border: #bdbdbd;
  }
  * { box-sizing: border-box; margin: 0; padding: 0; }
  html, body { width: 1200px; height: 900px; overflow: hidden; }
  body {
    background: var(--page);
    font-family: "Source Sans 3", Arial, sans-serif;
    font-weight: 400;
    color: var(--text);
    position: relative;
  }
  .window {
    position: absolute; left: 90px; top: 84px;
    width: 1020px; height: 789px;
    background: var(--page);
    box-shadow: 0 2px 10px rgba(0,0,0,.35);
  }
  .title-bar {
    position: absolute; left: 0; top: 0; width: 100%; height: 106px;
    background: var(--brand); color: #fff;
  }
  .title-bar h1 {
    font-weight: 300; font-size: 29px; text-align: center;
    line-height: 106px; letter-spacing: .2px;
  }
  .window-controls { position: absolute; top: 10px; right: 18px; display: flex; gap: 14px; }
  .window-controls svg { width: 24px; height: 24px; display: block; }

  .tab-bar { position: absolute; left: 0; top: 106px; width: 100%; height: 85px; }
  .tab {
    position: absolute; top: 15px; width: 130px; height: 54px;
    display: flex; align-items: center; justify-content: center;
    text-align: center; font-size: 17px; line-height: 22px;
    color: var(--brand); font-weight: 300;
  }
  .tab.is-active { border: 1.5px solid var(--brand); }
  .tab.is-disabled { color: var(--muted); }

  .content {
    position: absolute; left: 0; top: 191px; width: 100%; height: 501px;
    background: var(--divider);
  }
  .panel { position: absolute; background: var(--page); }
  .panel-clubs { left: 0; top: 7px; width: 396px; height: 489px; }
  .panel-duration { left: 403px; top: 7px; width: 296px; height: 252px; }
  .panel-participants { left: 706px; top: 7px; width: 314px; height: 252px; }
  .panel-discount { left: 403px; top: 266px; width: 296px; height: 230px; }
  .panel-registration { left: 706px; top: 266px; width: 314px; height: 230px; }

  .label, .panel-title {
    position: absolute; font-size: 17px; line-height: 20px;
    font-weight: 300; white-space: nowrap; color: var(--text);
  }
  .field {
    position: absolute; width: 57px; height: 23px;
    border: 1px solid var(--field-border);
    font-size: 16px; line-height: 21px; text-align: center; font-weight: 300;
  }
  .radio {
    position: absolute; width: 26px; height: 26px; border-radius: 50%;
    border: 1px solid var(--control-border); background: #fff;
    transform: translate(-50%, -50%);
  }
  .radio.is-checked::after {
    content: ""; position: absolute; left: 50%; top: 50%;
    width: 15px; height: 15px; border-radius: 50%;
    background: var(--brand); transform: translate(-50%, -50%);
  }
  .checkbox {
    position: absolute; width: 25px; height: 25px;
    border: 1px solid var(--control-border); background: #fff;
  }
  .rule { position: absolute; height: 1px; background: #9a9a9a; }

  .footer { position: absolute; left: 0; top: 692px; width: 100%; height: 97px; }
  .button {
    position: absolute; top: 21px; width: 131px; height: 55px;
    font-size: 17px; font-weight: 300; line-height: 55px; text-align: center;
  }
  .button-primary { left: 730px; background: var(--brand); color: #fff; }
  .button-secondary { left: 870px; border: 1px solid var(--brand); color: var(--text); }
</style>
</head>
<body>
<div class="window">
  <header class="title-bar">
    <h1>Course Template</h1>
    <div class="window-controls">
      <svg viewBox="0 0 24 24" aria-label="Minimize"><line x1="5" y1="12" x2="19" y2="12" stroke="#fff" stroke-width="2"/></svg>
      <svg viewBox="0 0 24 24" aria-label="Maximize"><rect x="6" y="6" width="12" height="12" fill="none" stroke="#fff" stroke-width="2"/></svg>
      <svg viewBox="0 0 24 24" aria-label="Close"><path d="M7 7 L17 17 M17 7 L7 17" stroke="#fff" stroke-width="2.2"/></svg>
    </div>
  </header>

  <nav class="tab-bar">
    <div class="tab is-active" style="left:6px">Template<br>Type</div>
    <div class="tab" style="left:138px">General</div>
    <div class="tab" style="left:269px">Finance</div>
    <div class="tab is-disabled" style="left:399px">Preliminary<br>Course</div>
    <div class="tab is-disabled" style="left:532px">Package</div>
    <div class="tab" style="left:663px">Learning<br>Goals</div>
    <div class="tab" style="left:794px">Remark</div>
  </nav>

  <main class="content">
    <section class="panel panel-clubs">
      <div class="panel-title" style="left:80px;top:62px">Number Of Clubs</div>
      <div class="field" style="left:80px;top:133px">0</div>
      <div class="label" style="left:152px;top:135px">Club</div>
      <span class="radio" style="left:258px;top:127px"></span>
      <div class="label" style="left:280px;top:117px">In Weeks</div>
      <span class="radio is-checked" style="left:258px;top:164px"></span>
      <div class="label" style="left:280px;top:154px">In Months</div>
      <div class="rule" style="left:74px;top:195px;width:300px"></div>
      <div class="label" style="left:81px;top:241px">Long</div>
      <div class="field" style="left:128px;top:242px;height:21px;line-height:19px">0</div>
      <span class="radio" style="left:258px;top:232px"></span>
      <div class="label" style="left:280px;top:222px">Weeks</div>
      <span class="radio is-checked" style="left:258px;top:270px"></span>
      <div class="label" style="left:280px;top:260px">Months</div>
    </section>

    <section class="panel panel-duration">
      <div class="panel-title" style="left:58px;top:62px">Club duration (unit)</div>
      <span class="radio" style="left:77px;top:141px"></span>
      <div class="field" style="left:116px;top:128px">0</div>
      <div class="label" style="left:185px;top:131px">Minutes</div>
      <span class="radio is-checked" style="left:77px;top:176px"></span>
      <div class="label" style="left:117px;top:166px">Individuals</div>
    </section>

    <section class="panel panel-participants">
      <div class="panel-title" style="left:60px;top:62px">Number Of Participants</div>
      <div class="field" style="left:59px;top:128px">0</div>
      <div class="label" style="left:121px;top:130px">Minimum</div>
      <div class="field" style="left:59px;top:163px">0</div>
      <div class="label" style="left:121px;top:165px">Maximum</div>
    </section>

    <section class="panel panel-discount">
      <div class="panel-title" style="left:58px;top:37px">Discount Group</div>
      <span class="checkbox" style="left:63px;top:106px"></span>
      <div class="label" style="left:114px;top:108px">Member</div>
    </section>

    <section class="panel panel-registration">
      <div class="panel-title" style="left:59px;top:37px">Registration Only For</div>
      <span class="checkbox" style="left:65px;top:106px"></span>
      <div class="label" style="left:113px;top:108px">Couple</div>
    </section>
  </main>

  <footer class="footer">
    <div class="button button-primary">Save</div>
    <div class="button button-secondary">Cancel</div>
  </footer>
</div>
</body>
</html>
```